Dorvel582 Smoke shop and Wine Store

DORVEL SMOKE SHOP & WINE INC

Smoke shop, Bill payments, unlock phones,Cellphones, Cellphone accessories and repair.
ADDRESS:
582 Harlow Ave11209Brooklyn, NY
phone # 3470194857
Mobile # 3472061639
E-mail: Dorvel5826@mailvista.test
Instagram: DORVELSMOKESHOP

we sell hookah and all hookah accessories and tobaccos. E-cigarettes, vapes, E-juice, vapes parts and replacements, unlocked phones, bill payments and international to-ups,

Target Market(s)

SMOKE sHOPS
Cell phones market

Industry/Entity Type

Shop

Contact Information for Business Card

Teodor Brask
3470194857
3472061639

Smoke Shop - Unlocked phones - Phone Accessories - phone repair - bill payments - unlock services.

Font styles to use
Decorative

Requirements
Must have
• - attractive colors and designs on the business card.
• - graphics
Nice to have
• Cellphone pics and graphs

```html
<!DOCTYPE html>
<html lang="en">
<head>
<meta charset="utf-8">
<title>Dorvel Smoke Shop &amp; Wine — Business Card</title>
<link rel="stylesheet" href="https://fonts.googleapis.com/css2?family=Chewy&family=Open+Sans:wght@600;700;800&display=swap">
<style>
  :root {
    --page-bg: #d9d4cc;
    --purple-deep: #2a1540;
    --purple-mid: #5b2a86;
    --purple-glow: #8a3f8f;
    --title-lilac: #b57ae8;
    --logo-gold: #f2b632;
    --band-black: #0b0b0c;
    --band-edge: #9ee03a;
    --name-gold: #f0b429;
    --contact-green: #a9e04a;
    --icon-gold: #f5b81c;
    --white: #ffffff;
  }
  * { margin: 0; padding: 0; box-sizing: border-box; }
  html, body {
    width: 1200px; height: 1023px; overflow: hidden;
    background: var(--page-bg);
  }
  .card {
    position: absolute; left: 100px; top: 226px;
    width: 1000px; height: 571px;
    border-radius: 6px; overflow: hidden;
    background: linear-gradient(160deg, var(--purple-deep) 0%, var(--purple-mid) 55%, var(--purple-glow) 100%);
    box-shadow: 0 18px 40px rgba(0,0,0,.35);
    font-family: "Open Sans", sans-serif;
  }
  .skyline {
    position: absolute; left: 0; top: 150px; width: 1000px; height: 240px;
    background: linear-gradient(180deg, rgba(120,60,140,0) 0%, rgba(60,30,80,.75) 60%, rgba(30,15,45,.9) 100%);
  }
  .wine-photo {
    position: absolute; left: 760px; top: 18px; width: 210px; height: 120px;
    border-radius: 10px;
    background: radial-gradient(ellipse at 50% 55%, #7a1a2e 0%, #3a0d1c 55%, rgba(40,10,30,0) 80%);
  }
  .product-photo {
    position: absolute; left: 40px; top: 232px; width: 160px; height: 110px;
    border-radius: 6px;
    background: linear-gradient(135deg, #2b2b30 0%, #55555c 60%, #c9c9c9 100%);
  }
  .brand {
    position: absolute; left: 60px; top: 40px;
    display: flex; align-items: center; gap: 12px;
  }
  .brand-dot {
    width: 22px; height: 22px; border-radius: 50%; background: var(--logo-gold);
  }
  .brand-name {
    font-weight: 800; font-size: 42px; line-height: 1; color: var(--logo-gold);
  }
  .shop-title {
    position: absolute; left: 0; width: 1000px; top: 140px; text-align: center;
    font-family: "Chewy", "Comic Sans MS", cursive; font-weight: 400;
    font-size: 64px; line-height: 1; letter-spacing: 2px;
    color: var(--title-lilac);
  }
  .services {
    position: absolute; left: 230px; top: 236px; width: 520px;
    color: var(--white); font-weight: 700; font-size: 16px; line-height: 26px;
    letter-spacing: .5px; text-transform: uppercase; white-space: nowrap;
  }
  .band { position: absolute; left: 0; top: 0; width: 1000px; height: 571px; }
  .holder-name {
    position: absolute; left: 60px; top: 440px; width: 310px;
    color: var(--name-gold); font-weight: 800; font-size: 34px; line-height: 1;
    text-transform: uppercase; letter-spacing: 1px; white-space: nowrap;
  }
  .divider {
    position: absolute; left: 395px; top: 408px; width: 2px; height: 100px;
    background: var(--name-gold); opacity: .8;
  }
  .contact {
    position: absolute; left: 425px; color: var(--contact-green);
    font-weight: 600; font-size: 22px; line-height: 1;
    display: flex; align-items: center; gap: 10px; white-space: nowrap;
  }
  .contact-phones { top: 420px; }
  .contact-address { top: 470px; text-transform: uppercase; }
  .phone-icon { width: 24px; height: 24px; flex: none; }
  .sep { color: var(--name-gold); margin: 0 6px; }
</style>
</head>
<body>
  <main class="card">
    <div class="skyline" role="img" aria-label="Night city skyline photo in purple tones"></div>
    <div class="wine-photo" role="img" aria-label="Photo of a red wine bottle and glass"></div>
    <div class="product-photo" role="img" aria-label="Photo of an e-cigarette pack and cigarette"></div>

    <div class="brand"><span class="brand-dot"></span><span class="brand-name">Dorvel</span></div>
    <h1 class="shop-title">SMOKE SHOP &amp; WINE</h1>
    <p class="services">Smoke Shop • Bill Payments • Unlock Phones<br>Cellphones • Cellphone Accessories and Repair</p>

    <svg class="band" viewBox="0 0 1000 571" aria-hidden="true">
      <path d="M0,390 Q520,370 1000,260 L1000,571 L0,571 Z" fill="var(--band-black)"/>
      <path d="M0,390 Q520,370 1000,260" fill="none" stroke="var(--band-edge)" stroke-width="5"/>
    </svg>

    <div class="holder-name">Teodor Brask</div>
    <div class="divider"></div>

    <div class="contact contact-phones">
      <svg class="phone-icon" viewBox="0 0 24 24"><rect width="24" height="24" rx="4" fill="var(--icon-gold)"/><path d="M8 5l2.5 3-1.5 1.5c.8 1.8 2.2 3.2 4 4l1.5-1.5 3 2.5-1.5 2.5C11 17 7 13 5.5 6.5z" fill="#111"/></svg>
      <span>3470194857</span><span class="sep">|</span>
      <svg class="phone-icon" viewBox="0 0 24 24"><rect width="24" height="24" rx="4" fill="var(--icon-gold)"/><path d="M8 5l2.5 3-1.5 1.5c.8 1.8 2.2 3.2 4 4l1.5-1.5 3 2.5-1.5 2.5C11 17 7 13 5.5 6.5z" fill="#111"/></svg>
      <span>3472061639</span>
    </div>
    <div class="contact contact-address">582 Harlow Ave11209Brooklyn, NY</div>
  </main>
</body>
</html>
```